Website design for labour force (commercial truck driver) company

Looking for a Wordpress template (or design files in conjunction with a free Wordpress template).
Company tag line:
Tenvora – On Demand, Professional Drivers
Real Drivers | Real Standards | Real Results
Logo design has already been completed and is attached

Company provides contract drivers to trucking companies. Target market is both the trucking companies looking for drivers and drivers looking for work.
Design to encompass header / footer and basic page design, navigation menu, home page, contact page. Customer will add content and additional pages over time.

```html
<!DOCTYPE html>
<html lang="en">
<head>
<meta charset="utf-8">
<title>Tenvora – On Demand, Professional Drivers</title>
<link href="https://fonts.googleapis.com/css2?family=Poppins:wght@300;400;500;600;700&display=swap" rel="stylesheet">
<style>
:root{
  --green:#128a68;
  --ink:#111111;
  --navy:#0b101d;
  --grey-bg:#f7f7f7;
  --text:#3a3a3a;
  --lime:#d9e86c;
  --white:#ffffff;
}
*{box-sizing:border-box;margin:0;padding:0}
html,body{width:1200px;height:3363px;overflow:hidden}
body{position:relative;font-family:"Poppins",sans-serif;color:var(--ink);background:var(--white)}
.abs{position:absolute}
.media{position:absolute;overflow:hidden}
.btn{position:absolute;display:flex;align-items:center;justify-content:center;border-radius:20px;font-weight:500;color:var(--white);background:var(--green);font-size:10.5px;text-decoration:none}
.line{display:block;white-space:nowrap}

/* hero */
.hero{position:absolute;left:0;top:0;width:1200px;height:740px;background:#000}
.hero-scene{position:absolute;left:0;top:0;width:1200px;height:740px;background:
  radial-gradient(ellipse 520px 340px at 880px 200px,#7d7a72 0%,#4b4840 35%,#1e1c19 70%,#000 100%)}
.hero-shapes{position:absolute;left:0;top:0}
.logo{position:absolute;left:252px;top:26px;display:flex;align-items:center;gap:10px;color:var(--white);font-weight:600;font-size:18px}
.logo-dot{width:28px;height:28px;border-radius:50%;background:var(--white)}
.nav{position:absolute;top:30px;left:623px;font-size:12.5px;color:var(--white)}
.nav a{color:var(--white);text-decoration:none;position:absolute;white-space:nowrap}
.hero-title{left:120px;top:165px;font-size:58px;line-height:66px;font-weight:300;color:var(--white);letter-spacing:-0.5px}
.hero-sub{left:122px;top:233px;font-size:18.5px;font-weight:300;color:var(--white);line-height:25px}
.btn-outline{left:120px;top:316px;width:180px;height:38px;background:transparent;border:1.5px solid var(--white);border-radius:22px;font-size:11px}
.hero-photo{left:61px;top:472px;width:488px;height:352px;border-radius:13px;background:linear-gradient(120deg,#cfd3d6 0%,#9aa3ab 35%,#6d7a86 60%,#d6d9dc 100%)}

/* about */
.about-title{left:252px;top:876px;font-size:40px;font-weight:300;line-height:45px;letter-spacing:-1.2px}
.about-rule{left:245px;top:1044px;width:187px;height:3px;background:var(--ink)}
.about-copy{left:550px;top:1001px;font-size:10.4px;line-height:16.8px;color:var(--text)}
.btn-about{left:544px;top:1153px;width:160px;height:34px}

/* vacancies */
.vacancies{position:absolute;left:0;top:1292px;width:1200px;height:693px;background:var(--grey-bg)}
.eyebrow{font-size:12.5px;color:var(--green);font-weight:400}
.vac-eyebrow{left:253px;top:1340px}
.vac-heading{left:254px;top:1360px;font-size:18.5px;font-weight:300}
.job-card{position:absolute;top:1437px;width:342px;height:228px;background:var(--white);border-radius:6px}
.job-type{position:absolute;left:34px;top:29px;font-size:9px;display:flex;align-items:center;gap:4px;color:var(--text)}
.job-type svg{width:10px;height:10px}
.job-title{position:absolute;left:34px;top:50px;font-size:17.5px;font-weight:700;line-height:22.5px;color:#1d2230}
.job-desc{position:absolute;left:36px;top:100px;font-size:10.5px;line-height:16.5px;color:var(--text)}
.job-card .btn{left:36px;top:168px;width:109px;height:29px;font-size:10px}
.jobs-cta-title{left:0;width:1200px;top:1770px;text-align:center;font-size:20.5px;font-weight:300}
.jobs-cta-sub{left:0;width:1200px;top:1808px;text-align:center;font-size:12px;color:var(--ink)}
.btn-jobs{left:526px;top:1841px;width:115px;height:34px}
.portrait{position:absolute;width:156px;height:226px;border-radius:78px;border:2px solid var(--green)}
.portrait.dark{border-color:var(--ink)}

/* testimonial */
.testimonial{position:absolute;left:0;top:2181px;width:1200px;height:360px;background:var(--green)}
.t-eyebrow{left:0;width:1200px;top:2245px;text-align:center;font-size:13.5px;color:var(--white)}
.t-rule{left:516px;top:2267px;width:175px;height:1.5px;background:var(--white)}
.t-quote{left:200px;width:800px;top:2296px;text-align:center;font-size:23px;line-height:30px;font-weight:300;color:var(--white)}
.t-name{left:0;width:1200px;top:2411px;text-align:center;font-size:11.5px;color:var(--lime)}
.arrow-btn{position:absolute;top:2315px;width:30px;height:30px}

/* commitment */
.c-frame{position:absolute}
.c-photo-main{left:234px;top:2602px;width:379px;height:213px;background:linear-gradient(135deg,#5d88b5 0%,#2d3a47 45%,#e2a53a 70%,#c9cdd2 100%)}
.c-photo-two{left:412px;top:2829px;width:201px;height:171px;background:linear-gradient(120deg,#e6e4de 0%,#b9b6ad 45%,#3c3b3a 70%,#c8a566 100%)}
.c-photo-three{left:628px;top:2852px;width:199px;height:132px;background:linear-gradient(120deg,#e0783a 0%,#d4d3ce 40%,#8a9298 70%,#e9e9e8 100%)}
.stat-label{left:245px;top:2881px;font-size:10px;color:var(--green)}
.stat-value{left:243px;top:2900px;font-size:46px;font-weight:700;letter-spacing:-1px}
.c-eyebrow{left:636px;top:2620px;font-size:10.5px;font-weight:600;color:var(--green)}
.c-copy{left:636px;top:2645px;font-size:11.2px;line-height:18.6px;color:var(--text)}

/* newsletter */
.news-shapes{position:absolute;left:0;top:3102px}
.news-photo{left:915px;top:3102px;width:285px;height:222px;background:linear-gradient(110deg,rgba(11,16,29,1) 0%,#3a4150 25%,#b98c6e 55%,#c9d7e2 80%,#e9eef2 100%)}
.n-eyebrow{left:434px;top:3157px;font-size:9.5px;color:var(--green)}
.n-title{left:434px;top:3176px;font-size:22px;font-weight:300;color:var(--white)}
.n-input{left:437px;top:3236px;font-size:10.5px;color:#b9bcc4}
.n-line{left:430px;top:3257px;width:428px;height:1px;background:#9ea2ab}
.n-arrow{left:842px;top:3238px;width:12px;height:12px}

/* footer */
.copyright{left:253px;top:3341px;font-size:9px;color:var(--ink)}
.socials{position:absolute;left:852px;top:3342px;display:flex;gap:8px}
.socials span{display:block;width:12px;height:12px;border-radius:2px;background:var(--ink)}
</style>
</head>
<body>

<!-- Hero -->
<section class="hero">
  <div class="hero-scene" role="img" aria-label="Red and white trucks driving along a curving highway through trees"></div>
  <svg class="hero-shapes" width="1200" height="740" viewBox="0 0 1200 740" aria-hidden="true">
    <path d="M626 432 H1060 Q1170 432 1200 522 V740 H600 V458 A26 26 0 0 1 626 432 Z" fill="#ffffff"/>
    <path d="M600 512 H713 A21.5 21.5 0 0 0 713 555 H1004 C1074 555 1114 600 1114 648 C1114 698 1074 740 1004 740 H600 Z" fill="#000000"/>
    <path d="M590 479 H795 A16.5 16.5 0 0 1 795 512 H590 Z" fill="#000000"/>
  </svg>
  <div class="logo"><span class="logo-dot"></span>Tenvora</div>
  <nav class="nav">
    <a href="#" style="left:0">Home</a>
    <a href="#" style="left:73px">About Us</a>
    <a href="#" style="left:163px">Contact Us</a>
    <a href="#" style="left:259px">Search Jobs</a>
  </nav>
  <h1 class="abs hero-title">Tenvora</h1>
  <p class="abs hero-sub">On Demand, Professional Drivers<br>Real Drivers | Real Standards | Real Results</p>
  <a class="btn btn-outline" href="#">Explore Opportunities</a>
</section>
<div class="media hero-photo" role="img" aria-label="Smiling truck driver leaning out of a white truck cab window"></div>

<!-- About -->
<h2 class="abs about-title">
  <span class="line">Tenvora&nbsp; is an agency for motivated</span>
  <span class="line">drivers who seek the freedom to choose</span>
  <span class="line">their path.</span>
</h2>
<div class="abs about-rule"></div>
<p class="abs about-copy">
  <span class="line">Whether you’re seeking a stable position with consistent hours or</span>
  <span class="line">looking to earn extra income on a flexible schedule, Keystone Transport</span>
  <span class="line">Staffing offers a variety of opportunities to suit your needs. We</span>
  <span class="line">understand that every driver has different goals, which is why we</span>
  <span class="line">provide options for both short-term flexibility and long-term stability.</span>
  <span class="line">With a wide range of assignments, you can choose what works best for</span>
  <span class="line">you while enjoying the support of a dedicated team behind you.</span>
</p>
<a class="btn btn-about" href="#">Read more about us</a>

<!-- Vacancies -->
<section class="vacancies"></section>
<p class="abs eyebrow vac-eyebrow">Our Featured Vacancies</p>
<h2 class="abs vac-heading">We offer diverse job opportunities that match your skills and aspirations.</h2>

<article class="job-card" style="left:253px">
  <div class="job-type"><svg viewBox="0 0 10 10"><circle cx="5" cy="5" r="4.2" fill="none" stroke="#333" stroke-width="1"/><path d="M5 2.6V5l1.6 1" fill="none" stroke="#333" stroke-width="1"/></svg>Fulltime</div>
  <h3 class="job-title">Driver CE supermarket<br>distribution</h3>
  <p class="job-desc"><span class="line">Our client is a leading logistics service provider in</span><span class="line">the Netherlands, offering comprehensive solutions</span><span class="line">in transport, warehousing, value-added logistics</span></p>
  <a class="btn" href="#">Contact Us</a>
</article>
<article class="job-card" style="left:606px">
  <div class="job-type"><svg viewBox="0 0 10 10"><circle cx="5" cy="5" r="4.2" fill="none" stroke="#333" stroke-width="1"/><path d="M5 2.6V5l1.6 1" fill="none" stroke="#333" stroke-width="1"/></svg>Fulltime</div>
  <h3 class="job-title">Driver CE supermarket<br>distribution</h3>
  <p class="job-desc"><span class="line">Our client is a leading logistics service provider in</span><span class="line">the Netherlands, offering comprehensive solutions</span><span class="line">in transport, warehousing, value-added logistics</span></p>
  <a class="btn" href="#">Contact Us</a>
</article>

<h2 class="abs jobs-cta-title">Looking For Driver Jobs?</h2>
<p class="abs jobs-cta-sub">Join a team that values your talents and supports your journey toward success!</p>
<a class="btn btn-jobs" href="#">Contact Us</a>

<div class="portrait" style="left:268px;top:1900px;background:linear-gradient(180deg,#dfe3e6 0%,#b9c1c8 50%,#8c3a3a 100%)" role="img" aria-label="Older truck driver in a checked shirt with arms crossed"></div>
<div class="portrait dark" style="left:436px;top:1918px;background:linear-gradient(180deg,#8c8f8f 0%,#5a5350 50%,#9c6a5e 100%)" role="img" aria-label="Driver on the phone standing beside his truck"></div>
<div class="portrait" style="left:606px;top:1900px;background:linear-gradient(180deg,#7fa6c8 0%,#4d5a68 50%,#e27a2e 100%)" role="img" aria-label="Driver in an orange safety vest standing by a truck"></div>
<div class="portrait dark" style="left:776px;top:1916px;background:linear-gradient(180deg,#6a5a45 0%,#8d7a5e 50%,#c2b64a 100%)" role="img" aria-label="Bearded driver in a beanie and hi-vis vest inside a cab"></div>

<!-- Testimonial -->
<section class="testimonial"></section>
<p class="abs t-eyebrow">Hear From Our Drivers</p>
<div class="abs t-rule"></div>
<p class="abs t-quote">
  <span class="line">Connecting Drivers with great companies, creates</span>
  <span class="line">great opportunities for future employment and good</span>
  <span class="line">pay rates. Very flexible for home times.</span>
</p>
<p class="abs t-name">Marcus Hale</p>
<svg class="arrow-btn" style="left:255px" viewBox="0 0 30 30" aria-label="Previous"><circle cx="15" cy="15" r="13.5" fill="none" stroke="#fff" stroke-width="1.6"/><path d="M21 15H9M13.5 10.5L9 15l4.5 4.5" fill="none" stroke="#fff" stroke-width="1.6" stroke-linecap="round" stroke-linejoin="round"/></svg>
<svg class="arrow-btn" style="left:947px" viewBox="0 0 30 30" aria-label="Next"><circle cx="15" cy="15" r="13.5" fill="none" stroke="#fff" stroke-width="1.6"/><path d="M9 15h12M16.5 10.5L21 15l-4.5 4.5" fill="none" stroke="#fff" stroke-width="1.6" stroke-linecap="round" stroke-linejoin="round"/></svg>
<svg class="abs" style="left:0;top:2460px" width="1200" height="82" viewBox="0 2460 1200 82" aria-hidden="true">
  <path d="M890 2465 H1160 Q1190 2465 1200 2480 V2542 H870 V2484 A19 19 0 0 1 890 2465 Z" fill="#ffffff"/>
  <path d="M860 2503 H986 A19 19 0 0 1 986 2541 H860 Z" fill="#128a68"/>
</svg>

<!-- Commitment -->
<svg class="c-frame" style="left:0;top:2770px" width="500" height="290" viewBox="0 2770 500 290" aria-hidden="true">
  <path d="M234 2779 H209 V3049 H488 V2995" fill="none" stroke="#111" stroke-width="2.5"/>
</svg>
<div class="media c-photo-main" role="img" aria-label="Cheerful driver in a cap and hi-vis jacket holding a phone at the wheel"></div>
<div class="media c-photo-two" role="img" aria-label="Smiling driver standing in front of parked trucks"></div>
<div class="media c-photo-three" role="img" aria-label="Driver in a hard hat giving a thumbs up from an orange truck cab"></div>
<p class="abs stat-label">Drivers joined us</p>
<p class="abs stat-value">13,000</p>
<p class="abs c-eyebrow">Our Commitment</p>
<p class="abs c-copy">
  <span class="line">Our commitment to understanding the unique demands of</span>
  <span class="line">each sector allows us to deliver staff who are not just</span>
  <span class="line">qualified, but truly excel in their roles. Our goal is to provide</span>
  <span class="line">more than just workers – we aim to deliver workforce</span>
  <span class="line">solutions that seamlessly integrate with your operations,</span>
  <span class="line">driving productivity, innovation, and ultimately, your</span>
  <span class="line">business success.</span>
</p>

<!-- Newsletter -->
<svg class="news-shapes" width="1200" height="222" viewBox="0 3102 1200 222" aria-hidden="true">
  <path d="M305 3102 H1200 V3324 H115 A79 79 0 0 1 115 3166 H394 A18 18 0 0 0 394 3130 H305 A14 14 0 0 1 305 3102 Z" fill="#0b101d"/>
</svg>
<div class="media news-photo" role="img" aria-label="Happy driver in a plaid shirt waving from a truck cab"></div>
<p class="abs n-eyebrow">Don’t let your perfect job drive by.</p>
<h2 class="abs n-title">Find your next great opportunity!</h2>
<p class="abs n-input">Enter your email</p>
<div class="abs n-line"></div>
<svg class="abs n-arrow" viewBox="0 0 12 12" aria-label="Submit"><path d="M2 6h8M7 3l3 3-3 3" fill="none" stroke="#fff" stroke-width="1.3" stroke-linecap="round" stroke-linejoin="round"/></svg>

<!-- Footer -->
<p class="abs copyright">Copyright © 2025 Tenvora, All rights reserved.</p>
<div class="socials" aria-label="Social links"><span></span><span></span><span></span><span></span><span></span></div>

</body>
</html>
```